New business card design needed for Trucking/Staffing company!

I am looking for a business card design. The business name is Harbor Lane Freightworks, LLC. This company is a staffing company for commercial drivers/truck drivers. Most of our customers are trucking/supply companies. Our colors are blue/black/white/grey. The info I have on my current business cards is
-Spot for a name
-2 lines for an address
-3 lines for Office, cell, and fax
-email
-website(currently on backside of card with logo but can go anywhere)
Updates

Project Deadline Extended
Reason: Open to more designs

Target Market(s)

Trucking companies, building supply companies

Industry/Entity Type

Business

Contact Information for Business Card

Edgy but professional

Font styles to use
Other font styles liked:
• Open to suggestions

Colors
0555a3
000000
ffffff
9d9d9d

Requirements
Must have
• Must have the logo incorporated

```html
<!DOCTYPE html>
<html lang="en">
<head>
<meta charset="UTF-8">
<title>Harbor Lane Freightworks – Business Card</title>
<link href="https://fonts.googleapis.com/css2?family=Open+Sans:wght@400;600;700&family=Audiowide&display=swap" rel="stylesheet">
<style>
  :root {
    --blue: #0555a3;
    --blue-deep: #1b2a8f;
    --blue-bright: #3f5fd0;
    --black: #000000;
    --charcoal: #1a1a1a;
    --grey: #9d9d9d;
    --white: #ffffff;
    --stage: #e9e9ec;
  }
  * { margin: 0; padding: 0; box-sizing: border-box; }
  html, body { width: 1200px; height: 913px; overflow: hidden; }
  body {
    background: var(--stage);
    font-family: "Open Sans", Arial, sans-serif;
    display: flex;
    align-items: center;
    justify-content: center;
    gap: 40px;
  }
  .card {
    position: relative;
    width: 540px;
    height: 309px;
    overflow: hidden;
    box-shadow: 0 8px 24px rgba(0,0,0,.25);
  }

  /* Front */
  .card-front {
    background: linear-gradient(135deg, var(--blue-bright) 0%, var(--blue-deep) 55%, #16237a 100%);
    color: var(--white);
  }
  .road { position: absolute; background: var(--white); }
  .road-vertical { top: 0; bottom: 0; right: 36px; width: 30px; }
  .road-horizontal { left: 0; right: 0; top: 200px; height: 16px; }
  .road-dash { position: absolute; border-color: var(--grey); border-style: dashed; }
  .road-vertical .road-dash { top: 0; bottom: 0; left: 14px; border-width: 0 0 0 2px; }
  .road-horizontal .road-dash { left: 0; right: 0; top: 7px; border-width: 2px 0 0 0; }
  .road-marker {
    position: absolute; left: 10px; top: 188px;
    width: 14px; height: 14px; background: var(--white);
  }
  .brand-front {
    position: absolute; left: 60px; top: 64px;
    display: flex; align-items: center; gap: 10px;
  }
  .brand-square { width: 14px; height: 14px; background: var(--white); }
  .brand-name {
    font-family: "Audiowide", "Open Sans", sans-serif;
    font-size: 22px; letter-spacing: 1px; color: var(--white);
    line-height: 1.15;
  }
  .person-name {
    position: absolute; left: 32px; top: 176px;
    font-size: 15px; color: var(--black); letter-spacing: .5px;
  }
  .person-name strong { font-weight: 700; }
  .contact-list {
    position: absolute; right: 78px; top: 104px;
    text-align: right; font-size: 11.5px; line-height: 16px;
  }
  .icon-column {
    position: absolute; right: 37px; top: 104px; width: 28px;
    display: flex; flex-direction: column; align-items: center; gap: 4px;
  }
  .icon-column svg { width: 12px; height: 12px; fill: none; stroke: var(--charcoal); stroke-width: 1.6; }
  .address {
    position: absolute; left: 32px; top: 236px;
    font-size: 12.5px; line-height: 18px;
  }

  /* Back */
  .card-back {
    background: linear-gradient(160deg, #5a5a5a 0%, #2b2b2b 45%, #0d0d0d 100%);
    display: flex; align-items: center; justify-content: center;
  }
  .brand-back { display: flex; align-items: center; gap: 14px; }
  .brand-back .brand-square { width: 18px; height: 18px; background: var(--blue-bright); }
  .brand-back-name {
    font-family: "Audiowide", "Open Sans", sans-serif;
    font-size: 26px; letter-spacing: 1px; color: var(--blue-bright);
    line-height: 1.2;
  }
</style>
</head>
<body>

  <section class="card card-front" aria-label="Business card front">
    <div class="road road-horizontal"><span class="road-dash"></span></div>
    <div class="road road-vertical"><span class="road-dash"></span></div>
    <div class="road-marker"></div>

    <div class="brand-front">
      <span class="brand-square"></span>
      <span class="brand-name">HARBOR LANE<br>FREIGHTWORKS, LLC</span>
    </div>

    <p class="person-name"><strong>DANA</strong> REYES</p>

    <div class="contact-list">
      <p>+1 555-0142</p>
      <p>+1 555-0187</p>
      <p>+1 555-0163</p>
      <p>dana@harborlanefreight.com</p>
      <p>www.harborlanefreight.com</p>
    </div>

    <div class="icon-column" aria-hidden="true">
      <svg viewBox="0 0 12 12"><path d="M3 1h2l1 3-1.5 1a6 6 0 0 0 2.5 2.5L8 6l3 1v2a2 2 0 0 1-2 2A8 8 0 0 1 1 3a2 2 0 0 1 2-2z"/></svg>
      <svg viewBox="0 0 12 12"><rect x="3" y="1" width="6" height="10" rx="1"/><line x1="5" y1="9" x2="7" y2="9"/></svg>
      <svg viewBox="0 0 12 12"><rect x="1" y="4" width="10" height="6"/><rect x="3" y="1" width="6" height="3"/></svg>
      <svg viewBox="0 0 12 12"><rect x="1" y="2.5" width="10" height="7"/><path d="M1 2.5l5 4 5-4"/></svg>
      <svg viewBox="0 0 12 12"><circle cx="6" cy="6" r="5"/><path d="M1 6h10M6 1c-2.5 3-2.5 7 0 10M6 1c2.5 3 2.5 7 0 10"/></svg>
    </div>

    <div class="address">
      <p>48 Quay Road</p>
      <p>Millbrook, PA 17000</p>
    </div>
  </section>

  <section class="card card-back" aria-label="Business card back">
    <div class="brand-back">
      <span class="brand-square"></span>
      <span class="brand-back-name">HARBOR LANE<br>FREIGHTWORKS, LLC</span>
    </div>
  </section>

</body>
</html>
```